International Marketing Company - Web Design Project

kVesta is a well-funded start up in London developing an Online Marketing Platform for small businesses in Europe.

We require a large number of high quality business web designs for our business website builder. Our business websites are completely integrated into our Online Marketing systems and therefore it is important for designers to comply with our Design Guidelines.

This initial contest is a trial for us to open up the design process to top designers for the Builders vertical (e.g. Builders, Electricians, Plumbers, Flooring, etc.). We have implemented a base html structure and design and included them in the files.

Use your creativity to design new and fresh designs based on the included elements (e.g. testimonials, business description, etc).

We will award the stated prize money for the top three designs.

Any designers that submit designs we feel are of a high enough quality but do not make the top 3 could still be compensated and WILL be invited to participate in our next vertical competition.

Therefore, we encourage designers to submit as many designs as possible as we may award up to 25 designs.

Submissions will be reviewed daily and feedback provided where possible.

Designers who can also code will have the options to implement their designs for an additional fee.

Good luck!
Updates

There has been a mistake made in regard to the prize. Pixel Harbor should have it fixed soon.

1st place = £350
2nd place = £250
3rd Place = £150

Thanks,
Dorian
25/11/2011

UPDATE:

1st place will win £350
2nd place will win £250
3rd place will win £150

Everything else is as to the specification.

Thanks
Dorian

Target Market(s)

Builders, Electricians, Plumbers, Tradesman, Small construction companies

Industry/Entity Type

Business

Requirements
Must have
• Totally new designs based around the elements we want to show on each page.

We are looking for something different to the design we already have. But you can use that as a starting point.

Use the included files to see what is required for each page. Here is a brief outline:

Homepage - Testimonials, News, Business Description, Latest Projects and Call to action

About-Us - Team Summary, About the Business and a call to action

Projects Page - Project Details (Oage Title and description), Each project needs a title, content and 2 images.

Testimonials Page - The testifiers name and their comment

Contacts Page - Trovix Map, Company address, business hours, contact form and a call to action.

Please submit final designs in Photoshop or Fireworks format.

Each page has a set of elements. These element must feature in the design of that page. See supporting documents for page details.

All elements must be included in your design. Please do not add any extra element.

Professional look and feel
Nice to have
• Design variations:
Full width designs
Boxed Designs
With AND without carousels
OR static images
Good use of stock images.

Creative use of the elements, dont be restricted/influenced by the default design we have already

Designs based on the 960 grid

```html
<!DOCTYPE html>
<html lang="en">
<head>
<meta charset="utf-8">
<title>QT Builders</title>
<link rel="stylesheet" href="https://fonts.googleapis.com/css2?family=Arimo:wght@400;700&family=PT+Sans:wght@400;700&display=swap">
<style>
:root{
  --page:#e4e9eb;
  --card:#ffffff;
  --ink:#5b6369;
  --ink-soft:#6f7b84;
  --ink-dark:#3f4a52;
  --rule:#c9cfd3;
  --nav-top:#9aa8b0;
  --nav-bottom:#6e7d87;
  --orange:#f18e1f;
  --orange-light:#fbb040;
  --link:#1a8fc9;
}
*{box-sizing:border-box;margin:0;padding:0}
html,body{width:1175px;height:1200px;overflow:hidden}
body{background:var(--page);font-family:"Arimo",Arial,sans-serif;color:var(--ink);position:relative}
.abs{position:absolute}
.brand{left:46px;top:34px;font-size:24px;color:#4a5560;letter-spacing:.5px}
.phone-icon{left:942px;top:24px;width:86px;height:62px}
.nav{left:42px;top:92px;width:1098px;height:46px;border-radius:6px;
  background:linear-gradient(var(--nav-top),var(--nav-bottom));box-shadow:0 1px 2px rgba(0,0,0,.2)}
.nav a{position:absolute;top:0;line-height:46px;color:#fff;font-size:17px;text-decoration:none;transform:translateX(-50%)}
.nav .sep{position:absolute;top:6px;width:1px;height:34px;background:rgba(255,255,255,.25)}
.nav .call{position:absolute;left:810px;top:0;line-height:46px;font-size:24px;color:#fff;white-space:nowrap}
.card{background:var(--card);border-radius:7px;box-shadow:0 0 3px rgba(0,0,0,.08)}
.hero{left:42px;top:160px;width:1098px;height:632px}
.hero-band{left:0;top:0;width:1098px;height:426px;border-radius:7px 7px 0 0;
  background:linear-gradient(#eff3f5,#c8d8df)}
.hero-title{left:24px;top:12px;width:240px;font-size:32px;line-height:41px;color:#666e73;font-weight:400}
.cta{left:14px;top:320px;width:251px;height:83px;border-radius:10px;
  background:linear-gradient(var(--orange-light),var(--orange));color:#fff}
.cta svg{position:absolute;left:16px;top:21px}
.cta .div{position:absolute;left:65px;top:12px;width:1px;height:59px;background:rgba(255,255,255,.7)}
.cta .l1{position:absolute;left:76px;top:15px;font-size:22px;font-weight:700}
.cta .l2{position:absolute;left:84px;top:45px;font-size:15px}
.hero-photo{left:280px;top:14px;width:807px;height:398px;
  background:linear-gradient(#4f74a8 0%,#5b80b4 55%,#a97e5e 82%,#8c7f76 100%)}
.projects-title{left:0;top:437px;width:1098px;text-align:center;font-size:21px;color:var(--ink-soft);font-weight:400}
.projects-rule{left:56px;top:465px;width:988px;height:1px;background:var(--rule)}
.thumb{top:486px;width:172px;height:114px}
.caption{top:606px;width:220px;margin-left:-24px;text-align:center;font-family:"PT Sans",sans-serif;font-size:13px;color:var(--ink)}
.info{left:42px;top:814px;width:1098px;height:297px}
.welcome{left:60px;top:16px;font-size:27px;color:var(--orange);font-weight:400}
.rule{height:1px;background:var(--rule)}
.body-text{font-size:15px;line-height:19px;color:var(--ink)}
.col-head{font-family:"PT Sans",sans-serif;font-weight:700;font-size:11.5px;color:#7a8287;letter-spacing:.5px;text-transform:uppercase}
.small{font-size:12.8px;line-height:16px;color:var(--ink)}
.small p{margin-bottom:14px}
.more{color:var(--link);font-size:11px;text-decoration:none;border-bottom:1px solid var(--link)}
.name{font-size:11px;font-weight:700;color:var(--ink-dark);display:block;line-height:13px}
.footer{left:42px;top:1134px;width:1098px;height:43px;font-size:13px;color:#7a8287}
.footer span{position:absolute;top:14px}
.footer .admin{border-bottom:1px solid #7a8287}
</style>
</head>
<body>
<div class="abs brand">YOUR LOGO</div>

<svg class="abs phone-icon" viewBox="0 0 86 62" aria-hidden="true">
  <defs><linearGradient id="ph" x1="0" y1="0" x2="0" y2="1"><stop offset="0" stop-color="#dfe4e7"/><stop offset="1" stop-color="#a9b3b9"/></linearGradient></defs>
  <path d="M6 20 Q6 4 43 4 Q80 4 80 20 L80 26 Q80 30 74 30 L64 30 Q60 30 60 24 L60 19 L26 19 L26 24 Q26 30 22 30 L12 30 Q6 30 6 26Z" fill="url(#ph)"/>
  <path d="M22 32 L64 32 L74 58 Q74 61 70 61 L16 61 Q12 61 12 58Z" fill="url(#ph)"/>
</svg>

<nav class="abs nav">
  <a style="left:62px">HOME</a><span class="sep" style="left:128px"></span>
  <a style="left:212px">ABOUT US</a><span class="sep" style="left:304px"></span>
  <a style="left:384px">TESTIMONIALS</a><span class="sep" style="left:464px"></span>
  <a style="left:552px">PORTFOLIO</a><span class="sep" style="left:625px"></span>
  <a style="left:706px">CONTACT</a>
  <span class="call">Call us at 020 7946 0321</span>
</nav>

<section class="abs card hero">
  <div class="abs hero-band"></div>
  <h1 class="abs hero-title">Lorem ipsum dolor sit amet, consectetuer adipiscing elit, sed diam nonummy nibh euismod.</h1>
  <div class="abs cta">
    <svg width="42" height="42" viewBox="0 0 42 42" aria-hidden="true">
      <circle cx="21" cy="21" r="18" fill="none" stroke="#fff" stroke-width="4"/>
      <path d="M21 10 V21 H29" fill="none" stroke="#fff" stroke-width="3.5" stroke-linecap="round"/>
    </svg>
    <span class="div"></span>
    <span class="l1">First line text</span>
    <span class="l2">Second line text</span>
  </div>
  <div class="abs hero-photo" role="img" aria-label="Builder in a hard hat laying bricks against a blue sky"></div>

  <h2 class="abs projects-title">See Our Latest Projects</h2>
  <div class="abs projects-rule"></div>

  <div class="abs thumb" style="left:58px;background:linear-gradient(#b98a5a,#7a5232)" role="img" aria-label="Restored kitchen with wooden cabinets"></div>
  <div class="abs caption" style="left:58px">House restoration in Crawley</div>
  <div class="abs thumb" style="left:329px;background:linear-gradient(#d8c6ad,#9c8a78)" role="img" aria-label="Loft bedroom with a double bed"></div>
  <div class="abs caption" style="left:329px">Loft conversion near Crawley</div>
  <div class="abs thumb" style="left:600px;background:linear-gradient(#cdb69a,#5e4230)" role="img" aria-label="Living room with brown sofas"></div>
  <div class="abs caption" style="left:600px">House restoration in Crawley</div>
  <div class="abs thumb" style="left:871px;background:linear-gradient(#b97a4e,#cfd0cc)" role="img" aria-label="Conservatory with leather sofas"></div>
  <div class="abs caption" style="left:871px">Loft conversion near Crawley</div>
</section>

<section class="abs card info">
  <h2 class="abs welcome">Welcome to QT Builders</h2>
  <div class="abs rule" style="left:60px;top:50px;width:386px"></div>
  <div class="abs body-text" style="left:60px;top:62px;width:386px">
    <p>Lorem ipsum dolor sit amet, consectetuer adipiscing elit, sed diam nonummy nibh euismo. Etiam varius sapien in turpis. Suspendisse eros nibh, cursus vel, malesuada id, ullamcorper.Lorem ipsum dolor sit amet, consectetuer adipiscing elit, sed diam nonummy nibh euismod.<br>Read <a class="more">more </a> about us.</p>
    <p style="margin-top:19px">Call QT Construction on 0165550192 now to discuss how we can help you. My quotes are always FREE with no obligation.</p>
  </div>

  <h3 class="abs col-head" style="left:502px;top:30px">Customers say...</h3>
  <div class="abs rule" style="left:500px;top:50px;width:274px"></div>
  <div class="abs small" style="left:502px;top:62px;width:240px">
    <p>Lorem ipsum dolor sit amet, consectetuer adipiscing elit, sed diam nonummy nibh <a class="more">more</a><span class="name">Mr. Halvorsen</span></p>
    <p>Lorem ipsum dolor sit amet, consectetuer adipiscing elit, sed diam nonummy nibh <a class="more">more</a><span class="name">Mr. Halvorsen</span></p>
    <p>Lorem ipsum dolor sit amet, consectetuer adipiscing elit, sed diam nonummy nibh euismod.<a class="more">more</a><span class="name">Mr. Halvorsen</span></p>
  </div>

  <h3 class="abs col-head" style="left:800px;top:30px">Latest news</h3>
  <div class="abs rule" style="left:798px;top:50px;width:272px"></div>
  <div class="abs small" style="left:800px;top:62px;width:240px">
    <p>Lorem ipsum dolor sit amet, consectetuer adipiscing elit, sed diam nonummy nibh euismod. <a class="more">more</a></p>
    <p>In varius laoreet ipsum, ut auctor arcu tristique ut. Aliquam erat volutpat. Quisque purus metus, cursus non commodo egestas, ultrices id nunc.<a class="more">more</a></p>
    <p>Lorem ipsum dolor sit amet, consectetuer adipiscing elit, sed diam nonummy nibh euismod.<a class="more">more</a></p>
  </div>
</section>

<footer class="abs card footer">
  <span style="left:14px">Managed by kVesta</span>
  <span style="left:178px">¦ <span class="admin" style="position:static">Admin</span></span>
  <span style="left:800px">© My Company. All rights reserved.</span>
</footer>
</body>
</html>
```